Construction Company Website Design

I need a Website Design for a Construction Company. I have attached logo and business card design files (a.i) to match styles and text for the website. I will need design for 3 pages:
1. A Home page
2. A secondary page (will be different information pages)
3. A contact page with submision form
Website to look professional and match the 'theme' across all pages, using main colours / reverse colours as per design files. Must be clear it is a construction related website without being over the top. Happy for the construction related details (whether that be images/outlines/backgrounds etc to be fairly subtle and not overbearing on the contect of the pages. It will be the content that will be most important, not the images within.

Content has not yet been fully completed but attached is a site map. Each page will need a space for the insertion of the relevant heading and associated content for that particular page. Example can be used as per attached map. If it is preferable to have content completed for this to be a more succesful project please advise and I will complete and submit.

Target Market(s)

Clients for potential construction projects. These could be a range of people. All would be very professional, well educated and put a substantial expection on the quality of website provided.

Industry/Entity Type

Construction

Number of Pages Required

3 page

Font styles to use
Serif
Sans Serif
Other font styles liked:
• fonts preferable as per design files provided unless designer beleives a different font would suit better

Requirements
Must have
• Colour scheme to match logo and business card files provided. Fonts that match as per provided files. Pages must be consistent with the theme carrying across all pages. All pages must have contact details at the bottom of the page.
• Contents of page 1 - 'Home page': multiple tab options / logo link
• Contents of page 2 - 'Secondary page': Top and side navigation / area for information and/or images.
• Contents of page - 'Contact us page': Top and side navigation / Submission form / area for logos such as linkdin, facebook etc.
Nice to have
• Would be good to have a or some generic construction related images - outlines / shadows / effects etc. These might be background images or outlines related to the relevant industry and are consistent across the pages. Could be outlines of buildings, images of men with hardhats etc etc. Good to see colour scheme as per design files used
Should not have
• No pictures of houses. Generally no photos. If any imagery of people must not show faces/details.

```html
<!DOCTYPE html>
<html lang="en">
<head>
<meta charset="utf-8">
<title>K.R.T Constructions</title>
<link href="https://fonts.googleapis.com/css2?family=Exo+2:wght@400;500;600;700&family=Open+Sans:wght@300;400;600&display=swap" rel="stylesheet">
<style>
:root{
  --blue:#13a3e8;
  --blue-dark:#0d8fd0;
  --ink:#2f3337;
  --text:#4a4f54;
  --muted:#9aa0a5;
  --topbar:#3a3a3a;
  --dark:#1f2021;
  --footer:#2d2d2d;
  --panel:#e8ecea;
  --card:#e9ecec;
  --white:#ffffff;
}
*{box-sizing:border-box;margin:0;padding:0}
html,body{width:1200px;height:2539px;overflow:hidden}
body{position:relative;background:var(--white);font-family:'Open Sans',Arial,sans-serif;color:var(--text)}
.abs{position:absolute}
.heading-font{font-family:'Exo 2',Arial,sans-serif}

/* top bar */
.topbar{left:0;top:0;width:1200px;height:24px;background:var(--topbar);color:#e6e6e6;font-size:11px}
.topbar .item{position:absolute;top:5px;display:flex;align-items:center;gap:6px}
.topbar svg{width:13px;height:13px}

/* header */
.header{left:0;top:24px;width:1200px;height:74px;background:var(--white)}
.brand{font-family:'Exo 2',Arial,sans-serif;font-weight:500;font-size:14px;letter-spacing:2px;color:#444}
.nav{position:absolute;top:30px;font-family:'Exo 2',Arial,sans-serif;font-size:12px;font-weight:500;color:#555;letter-spacing:.3px}
.nav.active{color:var(--blue)}
.nav-marker{left:537px;top:88px;width:22px;height:4px;background:var(--blue)}

/* hero */
.hero{left:0;top:98px;width:1200px;height:439px;background:linear-gradient(100deg,#c9d3da 0%,#e6ecf1 35%,#f2f5f8 55%,#b9c7d2 80%,#8ea2b2 100%)}
.hero-title{left:208px;top:258px;font-family:'Exo 2',Arial,sans-serif;font-weight:700;font-size:31px;color:#111;letter-spacing:.5px}
.hero-sub{left:208px;top:298px;font-size:22px;font-weight:300;color:#222}
.btn{position:absolute;height:30px;background:var(--blue);color:#fff;font-family:'Exo 2',Arial,sans-serif;font-weight:600;font-size:11px;letter-spacing:.5px;display:flex;align-items:center;justify-content:center;gap:5px}
.btn svg{width:11px;height:11px}
.btn.light{background:#fff;color:var(--blue)}
.slider-arrow{width:38px;height:37px;background:#3a3d40;display:flex;align-items:center;justify-content:center}
.slider-arrow svg{width:12px;height:12px}

.vline{width:2px;background:var(--blue)}

/* welcome */
.welcome{left:210px;top:525px;width:780px;height:328px;background:var(--panel);box-shadow:0 6px 14px rgba(0,0,0,.15);text-align:center}
.section-title{position:absolute;left:0;width:100%;text-align:center;font-family:'Exo 2',Arial,sans-serif;font-size:25px;letter-spacing:.5px}
.title-rule{position:absolute;width:64px;height:2px;background:var(--blue);left:50%;margin-left:-32px}
.welcome p{position:absolute;left:30px;right:30px;top:123px;font-size:10.5px;line-height:17px;color:#444}

/* services */
.services{left:0;top:841px;width:1200px;height:693px;background:radial-gradient(ellipse at 50% 60%,#3b3c3e 0%,#262728 45%,#161718 100%)}
.service-card{position:absolute;top:948px;width:191px;height:318px}
.service-card.featured{background:#fff;width:199px;left:602px}
.service-img{position:absolute;left:0;top:5px;width:191px;height:144px}
.service-card h3{position:absolute;left:0;top:168px;font-family:'Exo 2',Arial,sans-serif;font-weight:600;font-size:14px;color:#fff;letter-spacing:.5px}
.service-card p{position:absolute;left:0;top:195px;width:188px;font-size:10.5px;line-height:17.5px;color:#e4e4e4}
.service-card.featured h3{color:#222;left:6px}
.service-card.featured p{color:#444;left:6px}
.service-card.featured .service-img{left:4px;top:5px}

/* projects */
.projects-intro{left:200px;top:1366px;width:200px;height:209px;background:var(--blue);color:#fff}
.projects-intro h3{position:absolute;left:19px;top:30px;font-family:'Exo 2',Arial,sans-serif;font-weight:600;font-size:23px;line-height:24px}
.projects-intro .rule{position:absolute;left:19px;top:84px;width:62px;height:2px;background:#fff}
.projects-intro p{position:absolute;left:19px;top:100px;width:170px;font-size:10.5px;line-height:17px}
.project-img{position:absolute;top:1366px;width:198px;height:171px}
.project-caption{position:absolute;top:1537px;width:198px;height:38px;background:#0b0b0b;color:var(--blue);font-family:'Exo 2',Arial,sans-serif;font-size:11px;font-weight:500;text-align:center;line-height:38px}

/* testimonials */
.testimonial{position:absolute;top:1688px;width:391px;height:149px;background:var(--card)}
.testimonial p{position:absolute;left:20px;top:14px;width:350px;font-size:10.5px;line-height:17px;color:#444}
.testimonial .name{position:absolute;left:20px;top:101px;font-family:'Exo 2',Arial,sans-serif;font-weight:600;font-size:12px;color:#333}
.testimonial .role{position:absolute;left:20px;top:118px;font-size:10px;color:var(--muted)}
.avatar{position:absolute;width:50px;height:50px;border-radius:50%;border:3px solid #fff;background:linear-gradient(160deg,#c7b8a8,#7b6a5c)}
.t-arrow{width:26px;height:50px}

/* news */
.news-band{left:0;top:1917px;width:1200px;height:196px;background:linear-gradient(120deg,#1a1a1a 0%,#343231 40%,#262524 70%,#121212 100%)}
.news-card{position:absolute;top:2035px;width:247px;height:188px;background:#fff;border-top:4px solid var(--blue)}
.news-card.raised{box-shadow:0 6px 16px rgba(0,0,0,.18)}
.news-card .date{position:absolute;left:20px;top:24px;font-size:9.5px;color:var(--blue)}
.news-card h4{position:absolute;left:20px;top:41px;width:215px;font-family:'Exo 2',Arial,sans-serif;font-weight:600;font-size:12px;line-height:18px;color:#222}
.news-card p{position:absolute;left:20px;top:92px;width:215px;font-size:10.5px;line-height:18px;color:#555}

/* footer */
.footer{left:0;top:2328px;width:1200px;height:211px;background:var(--footer);color:#fff}
.footer h5{position:absolute;font-family:'Exo 2',Arial,sans-serif;font-weight:600;font-size:12px;letter-spacing:.3px}
.footer .links{position:absolute;left:482px;top:2062px}
.footer ul{list-style:none;position:absolute;left:482px;top:64px;font-size:11px;line-height:18.6px}
.footer .info{position:absolute;font-size:10.5px;line-height:17px}
.footer .icon{position:absolute;width:14px;height:14px}
.social{position:absolute;top:2389px;width:25px;height:25px;border:1.5px solid #fff;border-radius:50%}
.copyright{position:absolute;left:186px;top:2498px;font-size:10.5px;color:#eee}
</style>
</head>
<body>

<!-- top bar -->
<div class="abs topbar">
  <div class="item" style="left:736px">
    <svg viewBox="0 0 16 16" fill="none" stroke="#ddd" stroke-width="1.4"><path d="M3 2h3l1.5 3.5-2 1.3a8 8 0 0 0 3.7 3.7l1.3-2L14 10v3a1 1 0 0 1-1 1A11 11 0 0 1 2 3a1 1 0 0 1 1-1z"/></svg>
    <span>0400 123 456</span>
  </div>
  <div class="item" style="left:838px">
    <svg viewBox="0 0 16 16" fill="none" stroke="#ddd" stroke-width="1.4"><rect x="1.5" y="3.5" width="13" height="9"/><path d="M1.5 3.5 8 9l6.5-5.5"/></svg>
    <span>info@krtbuild.com.au</span>
  </div>
</div>

<!-- header -->
<header class="abs header">
  <div class="abs brand" style="left:186px;top:28px">K.R.T CONSTRUCTIONS</div>
  <span class="nav active" style="left:530px">HOME</span>
  <span class="nav" style="left:587px">ABOUT US</span>
  <span class="nav" style="left:669px">SERVICES</span>
  <span class="nav" style="left:747px">PROJECTS</span>
  <span class="nav" style="left:828px">CULTURE</span>
  <span class="nav" style="left:902px">NEWS</span>
  <span class="nav" style="left:962px">CONTACT</span>
</header>
<div class="abs nav-marker"></div>

<!-- hero -->
<section class="abs hero" role="img" aria-label="Photo of a tower crane over a building site against a pale sky"></section>
<h1 class="abs hero-title">LOREM IPSUM DOLOR</h1>
<div class="abs hero-sub">Ut enim ad minim veniam</div>
<div class="btn" style="left:210px;top:357px;width:105px">READ MORE <svg viewBox="0 0 12 12" fill="none" stroke="#fff" stroke-width="1.6"><path d="M1 6h9M6.5 2.5 10 6l-3.5 3.5"/></svg></div>
<div class="abs slider-arrow" style="left:20px;top:300px"><svg viewBox="0 0 12 12" fill="none" stroke="#fff" stroke-width="2"><path d="M8 1 3 6l5 5"/></svg></div>
<div class="abs slider-arrow" style="left:1142px;top:300px"><svg viewBox="0 0 12 12" fill="none" stroke="#fff" stroke-width="2"><path d="m4 1 5 5-5 5"/></svg></div>

<!-- welcome -->
<section class="abs welcome">
  <h2 class="section-title" style="top:58px;color:#333;font-weight:400">WELCOME TO <strong style="font-weight:700">K.R.T CONSTRUCTIONS</strong></h2>
  <div class="title-rule" style="top:99px"></div>
  <p>Lorem ipsum dolor sit amet, consectetur adipiscing elit, sed do eiusmod tempor incididunt ut labore et dolore magna aliqua. Ut enim ad minim veniam, quis nostrud exercitation ullamco laboris nisi ut aliquip ex ea commodo consequat. Duis aute irure dolor in reprehenderit in voluptate velit esse cillum dolore eu fugiat nulla pariatur. Excepteur sint occaecat cupidatat non proident, sunt in culpa qui officia deserunt mollit anim id est laborum. Sed ut perspiciatis unde omnis iste natus error sit voluptatem accusantium doloremque laudantium, totam rem aperiam, eaque ipsa quae ab illo inventore veritatis et quasi architecto beatae vitae dicta sunt explicabo.</p>
  <div class="btn" style="left:337px;top:239px;width:105px">READ MORE <svg viewBox="0 0 12 12" fill="none" stroke="#fff" stroke-width="1.6"><path d="M1 6h9M6.5 2.5 10 6l-3.5 3.5"/></svg></div>
</section>
<div class="abs vline" style="left:599px;top:500px;height:44px"></div>

<!-- services -->
<section class="abs services" role="img" aria-label="Dark photo of a staircase inside a building under construction"></section>
<div class="abs vline" style="left:599px;top:836px;height:40px"></div>
<h2 class="section-title" style="top:885px;color:#fff;font-weight:500">OUR SERVICES</h2>
<div class="title-rule" style="top:923px"></div>

<article class="service-card" style="left:200px">
  <div class="service-img" role="img" aria-label="Photo of glass office towers" style="background:linear-gradient(160deg,#6fc3ea,#1d6ea8 60%,#0f3f6a)"></div>
  <h3>COMMERCIAL</h3>
  <p>Lorem ipsum dolor sit amet, consectetur adipiscing elit, sed do eiusmod tempor incididunt ut labore et dolore magna aliqua.</p>
  <div class="btn" style="left:0;top:283px;width:105px">READ MORE <svg viewBox="0 0 12 12" fill="none" stroke="#fff" stroke-width="1.6"><path d="M1 6h9M6.5 2.5 10 6l-3.5 3.5"/></svg></div>
</article>
<article class="service-card" style="left:403px">
  <div class="service-img" role="img" aria-label="Rendering of a modern residential building" style="background:linear-gradient(160deg,#eef1f5,#b9c4cf 60%,#7d8c99)"></div>
  <h3>RESIDENTIAL</h3>
  <p>Lorem ipsum dolor sit amet, consectetur adipiscing elit, sed do eiusmod tempor incididunt ut labore et dolore magna aliqua.</p>
  <div class="btn" style="left:0;top:283px;width:105px">READ MORE <svg viewBox="0 0 12 12" fill="none" stroke="#fff" stroke-width="1.6"><path d="M1 6h9M6.5 2.5 10 6l-3.5 3.5"/></svg></div>
</article>
<article class="service-card featured">
  <div class="service-img" role="img" aria-label="Photo of a worker on a ladder doing maintenance" style="background:linear-gradient(160deg,#e3e6e8,#b3bac0 55%,#6d7a86)"></div>
  <h3>BUILDING MAINTENANCE</h3>
  <p>Lorem ipsum dolor sit amet, consectetur adipiscing elit, sed do eiusmod tempor incididunt ut labore et dolore magna aliqua.</p>
  <div class="btn" style="left:6px;top:283px;width:105px">READ MORE <svg viewBox="0 0 12 12" fill="none" stroke="#fff" stroke-width="1.6"><path d="M1 6h9M6.5 2.5 10 6l-3.5 3.5"/></svg></div>
</article>
<article class="service-card" style="left:809px">
  <div class="service-img" role="img" aria-label="Photo of hands reviewing project plans with boxes" style="background:linear-gradient(160deg,#f4c68a,#d9804a 55%,#8a4a2c)"></div>
  <h3>PROJECT MANAGEMENT</h3>
  <p>Lorem ipsum dolor sit amet, consectetur adipiscing elit, sed do eiusmod tempor incididunt ut labore et dolore magna aliqua.</p>
  <div class="btn" style="left:0;top:283px;width:105px">READ MORE <svg viewBox="0 0 12 12" fill="none" stroke="#fff" stroke-width="1.6"><path d="M1 6h9M6.5 2.5 10 6l-3.5 3.5"/></svg></div>
</article>

<!-- recent projects -->
<div class="abs" style="left:200px;top:1364px;width:800px;height:2px;background:#9aa3a8"></div>
<section class="abs projects-intro">
  <h3>RECENT<br>PROJECTS</h3>
  <div class="rule"></div>
  <p>Lorem ipsum dolor sit amet, consectetur adipiscing elit, sed do eiusmod tempor.</p>
  <div class="btn light" style="left:20px;top:159px;width:105px">VIEW MORE <svg viewBox="0 0 12 12" fill="none" stroke="#13a3e8" stroke-width="1.6"><path d="M1 6h9M6.5 2.5 10 6l-3.5 3.5"/></svg></div>
</section>
<div class="project-img" role="img" aria-label="Photo of a modern apartment building with trees" style="left:401px;background:linear-gradient(170deg,#c9d8e4,#8d9ea9 50%,#4d6a4c)"></div>
<div class="project-caption" style="left:401px">Lorem ipsum dolor</div>
<div class="project-img" role="img" aria-label="Photo of an apartment building facade at dusk" style="left:601px;background:linear-gradient(170deg,#5f7890,#6b5b43 55%,#2c2a26)"></div>
<div class="project-caption" style="left:601px">Lorem ipsum dolor</div>
<div class="project-img" role="img" aria-label="Photo of a tall residential tower" style="left:801px;background:linear-gradient(170deg,#d6dee6,#a1a6aa 55%,#5a5d60)"></div>
<div class="project-caption" style="left:801px">Lorem ipsum dolor</div>

<!-- testimonials -->
<h2 class="section-title" style="top:1622px;color:#333;font-weight:500">TESTIMONIALS</h2>
<div class="title-rule" style="top:1659px"></div>
<svg class="abs t-arrow" style="left:155px;top:1740px" viewBox="0 0 26 50" fill="none" stroke="#bfc4c8" stroke-width="2"><path d="M22 2 4 25l18 23"/></svg>
<svg class="abs t-arrow" style="left:1020px;top:1740px" viewBox="0 0 26 50" fill="none" stroke="#13a3e8" stroke-width="2"><path d="m4 2 18 23L4 48"/></svg>
<article class="testimonial" style="left:200px">
  <p>"Lorem ipsum dolor sit amet, consectetur adipiscing elit, sed do eiusmod tempor incididunt ut labore et dolore magna aliqua. Ut enim ad minim veniam, quis nostrud exercitation ullamco laboris nisi ut aliquip ex ea commodo consequat."</p>
  <div class="name">Sam Archer</div>
  <div class="role">Lorem ipsum</div>
</article>
<div class="avatar" role="img" aria-label="Client portrait" style="left:511px;top:1808px"></div>
<article class="testimonial" style="left:609px">
  <p>"Lorem ipsum dolor sit amet, consectetur adipiscing elit, sed do eiusmod tempor incididunt ut labore et dolore magna aliqua. Ut enim ad minim veniam, quis nostrud exercitation ullamco laboris nisi ut aliquip ex ea commodo consequat."</p>
  <div class="name">John Doe</div>
  <div class="role">Lorem ipsum</div>
</article>
<div class="avatar" role="img" aria-label="Client portrait" style="left:928px;top:1795px"></div>

<!-- latest news -->
<section class="abs news-band" role="img" aria-label="Dark photo of a construction worker in a hard hat"></section>
<div class="abs vline" style="left:599px;top:1896px;height:42px"></div>
<h2 class="section-title" style="top:1961px;color:#fff;font-weight:500">LATEST NEWS</h2>
<div class="title-rule" style="top:1999px"></div>

<article class="news-card" style="left:210px">
  <div class="date">APR 15, 2018</div>
  <h4>Lorem ipsum dolor sit amet, consectetur adipiscing elit</h4>
  <p>Duis aute irure dolor in reprehenderit in voluptate velit esse cillum dolore eu fugiat nulla pariatur. Excepteur sint occaecat cupidatat non proident. [...]</p>
</article>
<article class="news-card raised" style="left:476px">
  <div class="date">APR 15, 2018</div>
  <h4>Lorem ipsum dolor sit amet, consectetur adipiscing elit</h4>
  <p>Duis aute irure dolor in reprehenderit in voluptate velit esse cillum dolore eu fugiat nulla pariatur. Excepteur sint occaecat cupidatat non proident. [...]</p>
</article>
<article class="news-card" style="left:743px">
  <div class="date">APR 15, 2018</div>
  <h4>Lorem ipsum dolor sit amet, consectetur adipiscing elit</h4>
  <p>Duis aute irure dolor in reprehenderit in voluptate velit esse cillum dolore eu fugiat nulla pariatur. Excepteur sint occaecat cupidatat non proident. [...]</p>
</article>
<div class="btn" style="left:547px;top:2251px;width:106px">READ MORE <svg viewBox="0 0 12 12" fill="none" stroke="#fff" stroke-width="1.6"><path d="M1 6h9M6.5 2.5 10 6l-3.5 3.5"/></svg></div>

<!-- footer -->
<footer class="abs footer">
  <div class="abs brand" style="left:186px;top:42px;color:#fff">K.R.T CONSTRUCTIONS</div>
  <h5 style="left:482px;top:34px">QUICK LINKS</h5>
  <ul>
    <li>Home</li><li>About Us</li><li>Services</li><li>Projects</li><li>Culture</li><li>News</li><li>Contact</li>
  </ul>
  <h5 style="left:596px;top:34px">CONTACT</h5>
  <svg class="icon" style="left:598px;top:56px" viewBox="0 0 14 14" fill="none" stroke="#fff" stroke-width="1.2"><path d="M7 13s4-4.3 4-7.3a4 4 0 0 0-8 0C3 8.7 7 13 7 13z"/><circle cx="7" cy="5.7" r="1.5"/></svg>
  <div class="info" style="left:620px;top:53px">K.R.T Constructions Pty Limited<br>14 Harbour Street<br>Northbridge 2063</div>
  <svg class="icon" style="left:598px;top:126px" viewBox="0 0 16 16" fill="none" stroke="#fff" stroke-width="1.3"><path d="M3 2h3l1.5 3.5-2 1.3a8 8 0 0 0 3.7 3.7l1.3-2L14 10v3a1 1 0 0 1-1 1A11 11 0 0 1 2 3a1 1 0 0 1 1-1z"/></svg>
  <div class="info" style="left:620px;top:124px">0400 123 456</div>
  <svg class="icon" style="left:598px;top:163px" viewBox="0 0 16 16" fill="none" stroke="#fff" stroke-width="1.3"><rect x="1.5" y="3.5" width="13" height="9"/><path d="M1.5 3.5 8 9l6.5-5.5"/></svg>
  <div class="info" style="left:620px;top:161px">info@krtbuild.com.au</div>
  <h5 style="left:809px;top:34px">STAY IN TOUCH</h5>
</footer>
<div class="social" style="left:810px"></div>
<div class="social" style="left:840px"></div>
<div class="social" style="left:870px"></div>
<div class="social" style="left:900px"></div>
<div class="abs vline" style="left:599px;top:2306px;height:40px"></div>
<div class="copyright">© 2018 K.R.T Constructions All Rights Reserved.</div>

</body>
</html>
```